Velmora Business Card

We need a design for business cards for our new company. We are a resident safety and security company company that focuses on senior living communities. we provide Nurse call, Access control, CCTV, Wired and wireless network infrastructure, Wander Management, and much more!

Our logo is the circuit board shield. Representing our high tech security solutions. I would like the business card to bring the same theme with perhaps some circuit board traces around the card similar to our logo

```html
<!DOCTYPE html>
<html lang="en">
<head>
<meta charset="utf-8">
<title>Velmora Business Card</title>
<link rel="stylesheet" href="https://fonts.googleapis.com/css2?family=Montserrat:wght@300;400;700&display=swap">
<style>
  :root {
    --backdrop: #8fc3ea;
    --card-white: #ffffff;
    --brand-blue: #2a5cc8;
    --brand-cyan: #35b8ea;
    --card-blue: #2152c4;
    --card-blue-deep: #1c46ad;
    --trace-blue: #2a5fcf;
    --ink-light: #ffffff;
  }
  * { box-sizing: border-box; margin: 0; padding: 0; }
  html, body {
    width: 1200px;
    height: 988px;
    overflow: hidden;
    background: var(--backdrop);
    font-family: "Montserrat", sans-serif;
  }
  .canvas {
    width: 1200px;
    height: 988px;
    display: flex;
    align-items: center;
    justify-content: center;
    gap: 40px;
  }
  .card {
    position: relative;
    width: 500px;
    height: 286px;
    border-radius: 4px;
    overflow: hidden;
    box-shadow: 0 18px 40px rgba(20, 60, 120, 0.25);
  }
  .card-front {
    background: var(--card-white);
    display: flex;
    align-items: center;
    justify-content: center;
  }
  .brand {
    display: flex;
    align-items: center;
    gap: 16px;
  }
  .brand-dot {
    width: 56px;
    height: 56px;
    border-radius: 50%;
    background: var(--brand-blue);
  }
  .brand-name {
    font-weight: 700;
    font-size: 44px;
    color: var(--brand-blue);
    letter-spacing: 1px;
  }
  .brand-suffix {
    align-self: flex-end;
    margin-left: -10px;
    margin-bottom: 10px;
    font-size: 8px;
    font-weight: 400;
    color: var(--brand-blue);
  }
  .card-back {
    background: var(--card-blue);
    color: var(--ink-light);
  }
  .trace-field {
    position: absolute;
    inset: 0;
    background:
      radial-gradient(ellipse at 70% 20%, var(--trace-blue) 0%, transparent 60%),
      linear-gradient(160deg, var(--card-blue) 0%, var(--card-blue-deep) 100%);
  }
  .holder {
    position: absolute;
    left: 40px;
    top: 92px;
  }
  .holder-name {
    font-weight: 700;
    font-size: 26px;
    letter-spacing: 0.5px;
  }
  .holder-title {
    margin-top: 4px;
    margin-left: 70px;
    font-weight: 300;
    font-size: 14px;
    letter-spacing: 2px;
  }
  .phones {
    position: absolute;
    left: 40px;
    bottom: 32px;
    font-size: 13px;
    font-weight: 400;
    line-height: 1.45;
  }
  .web {
    position: absolute;
    right: 32px;
    top: 104px;
    text-align: right;
    font-size: 13px;
    font-weight: 400;
    line-height: 1.45;
  }
</style>
</head>
<body>
  <main class="canvas">
    <section class="card card-front">
      <div class="brand">
        <span class="brand-dot"></span>
        <span class="brand-name">Velmora</span>
        <span class="brand-suffix">LLC</span>
      </div>
    </section>

    <section class="card card-back">
      <div class="trace-field" role="img" aria-label="Subtle circuit board trace pattern across the card"></div>
      <div class="holder">
        <p class="holder-name">Martin Kovach</p>
        <p class="holder-title">President</p>
      </div>
      <div class="phones">
        <p>Main - (555) 945-0199</p>
        <p>Direct - (555) 696-0133</p>
      </div>
      <div class="web">
        <p>Martin@Velmora.com</p>
        <p>www.Velmora.com</p>
      </div>
    </section>
  </main>
</body>
</html>
```